Glow in the Dark Inks Sales Flyer - Targeted to the music industry

We need help!
We need a creative flyer to tell the music industry about our new, colorful glow in the dark inks that look amazing on T-shirts and concert merchandise.

The flyer will go to merchandising managers for bands around the world. The design needs to be hip and contemporary but not offensive. No f-bombs please! Size is 4” x 6” or 3” x 5”, and will be printed on card stock. Design can be both sides if you want. We expect color but black and white with some fluorescent accents could be cool. Surprise us.
Here’s some copy, and we can fill in the contact info when the design is close to final.

Help your fans get lit with branded T-shirts and merchandise that glows in the dark!

Let our new Starwell Pigments light up your next show!

Call us now –
Updates

Hello Designers.

Please keep in mind that although the thought of glow-in-the-dark may trigger a glowing, green color in your creative minds, StarWell Pigments has a wide variety of colors to bring to offer. So please be sure to show that it's not only green glow we are promoting but we have a wide range of colors that glow (including pink, purple, white that glow blue, blue, green, orange, yellow, etc.)

Thank you!

```html
<!DOCTYPE html>
<html lang="en">
<head>
<meta charset="utf-8">
<title>Glow Inks Flyer</title>
<link rel="stylesheet" href="https://fonts.googleapis.com/css2?family=Arimo&family=PT+Sans&display=swap">
<style>
  :root {
    --page: #ffffff;
    --card: #050505;
    --ink-white: #ffffff;
    --ghost: #2a2a2a;
    --pink: #d4509a;
    --teal: #3fbfae;
    --mint: #dff3e8;
    --cyan: #2ec8e0;
    --info-fill: #636466;
    --info-border: #7a5c48;
    --info-text: #111111;
  }
  * { margin: 0; padding: 0; box-sizing: border-box; }
  html, body { width: 1200px; height: 1077px; overflow: hidden; background: var(--page); }
  .canvas { position: relative; width: 1200px; height: 1077px; }

  .card { position: absolute; top: 306px; height: 694px; width: 461px; background: var(--card); overflow: hidden; }
  .card--front { left: 154px; }
  .card--back { left: 638px; }

  .figure-art {
    position: absolute; left: 40px; top: 0; width: 420px; height: 694px;
    border-radius: 45% 40% 0 0 / 20% 15% 0 0;
    background:
      radial-gradient(ellipse 90px 180px at 230px 540px, #c8d93c 0%, #9dbb3a 50%, rgba(200,120,50,0.8) 80%, transparent 100%),
      radial-gradient(ellipse 150px 90px at 240px 210px, rgba(46,200,224,0.9) 0%, rgba(46,200,224,0.4) 60%, transparent 100%),
      linear-gradient(160deg, #3a3a3a 0%, #1e1e1e 45%, #0c0c0c 100%);
  }
  .headline-glow {
    position: absolute; left: 20px; top: 60px;
    font-family: "PT Sans", sans-serif; font-size: 104px; line-height: 1;
    background: linear-gradient(90deg, var(--teal), var(--mint));
    -webkit-background-clip: text; background-clip: text; color: transparent;
    transform: rotate(-8deg); transform-origin: left bottom;
  }

  .splatter-art {
    position: absolute; left: 10px; top: 20px; width: 200px; height: 130px;
    border-radius: 50% 40% 60% 30%;
    background: radial-gradient(ellipse at 40% 40%, rgba(46,200,224,0.85), rgba(46,200,224,0.25) 60%, transparent 75%);
  }
  .headline-night {
    position: absolute; left: 24px; top: 38px;
    font-family: "PT Sans", sans-serif; font-size: 54px; line-height: 1; color: var(--pink);
    transform: rotate(-5deg); transform-origin: left bottom; white-space: nowrap;
  }
  .pitch {
    position: absolute; left: 0; width: 100%; top: 114px;
    font-family: "Arimo", sans-serif; font-size: 30px; line-height: 37.5px; letter-spacing: 1px;
    color: var(--ink-white); text-align: center;
    text-shadow: 4px 18px 0 var(--ghost);
  }
  .company-info {
    position: absolute; left: 28px; top: 563px; width: 416px; height: 105px;
    background: var(--info-fill); border: 4px dashed var(--info-border);
    display: flex; align-items: center; justify-content: center;
    font-family: "Arimo", sans-serif; font-size: 26px; color: var(--info-text);
  }
</style>
</head>
<body>
<div class="canvas">
  <section class="card card--front">
    <div class="figure-art" role="img" aria-label="Stylised illustration of a dancer in grey tones with glowing cyan highlights and a rainbow-coloured glowing garment"></div>
    <h1 class="headline-glow">glow!</h1>
  </section>

  <section class="card card--back">
    <div class="splatter-art" role="img" aria-label="Cyan paint splatter decoration"></div>
    <h2 class="headline-night">rules the night</h2>
    <p class="pitch">You need shirts<br>SURPRISING<br>to blow up colors,<br>even at NIGHT!.<br>Amazing for promote<br>your concert or event.<br>We have a wide<br>variety of&nbsp; glow inks,<br>just bring us your<br>design.</p>
    <div class="company-info">COMPANY INFO</div>
  </section>
</div>
</body>
</html>
```